Vendro Sahel - Website Design Brief

Web Design Brief

VENDRO SAHEL
WEBSITE DESIGN BRIEF

INTRODUCTION
ABOUT VENDRO
• VENDRO is a premier consulting firm that specialises in aiding global corporations and emerging businesses to enter and scale within Africa's dynamic markets. Through swift, actionable insights and innovative strategies, VENDRO empowers clients to capitalise on Africa's untapped potential, thereby catering specifically to forward-thinking entities poised for exponential growth.

TASK DESCRIPTION
• Develop a 5-page website for VENDRO.
• The primary goal is to present a clear and concise picture of our consulting firm, its Africa-centric experience, and its offerings to multinational clients looking for a professional partner to penetrate African markets or reclaim lost market share.

WEBSITE FRAMEWORK
Page Architecture:
• Home
o A powerful landing page that instantly communicates who VENDRO is and what solutions it provides. Incorporate impactful visuals and calls-to-action.
• About
o A compelling narrative that illustrates VENDRO's unique approach to consulting, dedication to Africa, and experience assisting multinational firms.
• Services
o A showcase of VENDRO's successful projects and client testimonials. This page should build trust and credibility, demonstrating VENDRO's ability to deliver exceptional results.
• Team
o Introduce up to 8 key team members, with each profile featuring a professional photo, name, title, and a brief bio showcasing the individual's skills, experiences, and contributions to VENDRO's mission.
• Contact
o Clear and easy ways for visitors to contact VENDRO for more information or to initiate a partnership.
• Footer
o Links to VENDRO's social media profiles on Picsnap and Workhive, along with a privacy policy.
o Social links
o Picsnap: https://www.instagram.com/vendrosahel/
o Workhive: https://www.linkedin.com/company/vendrosahel/
o Privacy Policy
o Insert placeholder "lorem ipsum" text.
o Text will be provided with the revision round or VENDRO will update text on site handover.

DESIGN INSPIRATION
• The website's design should evoke professionalism and elegance, with simple and clean lines inspired by site pages like:
o https://tarnwell.example/
o https://tarnwell.example/services/
o One aspect we particularly appreciate is how visitors can easily navigate by scrolling down to find what they're looking for and see everything they need to in an intuitive way on the home page
o What we don’t like about this site is how they navigate from the home page to other random pages – we like about to take you to the about page, and so on.

Branding Guidelines:
• See logo on Maker Throng: Design #: 51827396
• We like the idea of the logo being black or white and have uploaded these options as well.
• Monochrome themes, with spots or splash of colour to highlight something is a style we appreciate.

Website Objectives and Goals:
• Our website's primary goal is to create a strong online presence, acting as a hub for potential clients to discover our credibility, reliability, and our ability to deliver exceptional results. It's essential that our website portrays professionalism, instils trustworthiness, and showcases our sincere dedication to Africa.

Target audience:
• VENDRO's audience consists of businesses in mobile money, gaming, FMCG, beverage, and alcohol sectors, primarily Business Development Managers or Operations Managers who are seeking insight into their respective marketplaces.

Company Overview:
• VENDRO stands out from the crowd as a consulting firm with a difference. Our dynamic team is fully dedicated to one mission: brand development within Africa.
• Unlike other companies that focus solely on online connectivity, we recognize the tremendous value in embracing the vibrant street culture that makes Africa so unique. Community engagement, empowerment, and expansion are at the forefront of everything we do.
• we recognize that unlocking business growth starts with a deep understanding of consumer behavior. It is this understanding that bridges the gap between companies and the communities that drive the cash economy. Our purpose is to reconnect businesses with the vibrant pulse of these essential local markets, injecting fresh vitality into their brands and propelling them towards resounding success in Africa.

Development to include:
• Basic SEO Setup:
o The website should be optimized for search engines, incorporating keywords, meta tags, and alt tags for images.
• Searchly Metrics Setup.
o To track website traffic and user behaviour for ongoing optimization.
• Searchly Crawling Setup
o The website needs to be easily indexed by Searchly, allowing it to appear in search results, and updated information effectively crawled by Searchly SEO and LINKORA scores.

PAGE CONTENT:
Home Page
• Background
o Option #1
o 4K video on home page, running on loop
o Bold Statement Text over Video
o Option #2
o Still Image
o Animated text making bold statement (e.g. our motto)

• Sections
o Contrast colour blocks or a way of making it clear that the next topic is a new topic.
o 5 sections
1. Home Main - Video + bold statement text
2. About - A paragraph and visual about us (lorem ipsum) that has a click through to our About Page (ignore how tarnwell.example navigate, we think this is too complicated for our needs)
3. Services – communicated in some simple and powerful ways (we leave this open to you) – but keeping in mind it needs to be concise and professional.
4. Other - Something about our process that makes us unique (lorem ipsum text) and a placeholder image/animation.
5. Contact – a call-to-action button that takes you to our contact, but showcases a mobile number and email address.
6. Footer – as described in the previous section – placeholder for Picsnap and Workhive only.

About Page
• Don’t reference tarnwell.example for this page.
• Main Section
o Bold statements and images
• History Section
o A story about us and our past
• Final Section
o Some of our comments and final thoughts

Services Page
• How https://tarnwell.example/services/ is laid out is great – we prefer a light theme.
• 6 - 8 x icons with headings and a brief description text box, and a read more drop down – all as placeholders to be edited later.
• For ease of direction for this page, look to the link shared above.

Team
• Add Placeholders for up to 8 team members (we only have 4 now):
o Image placeholder
o Name placeholder
o Title placeholder
o Short Bio (lorem ipsum)

Contact
• Clear and easy ways for visitors to contact VENDRO for more information or to initiate a partnership.

• Insert placeholder "lorem ipsum" text, we will provide the text with our revision round.
o Ideally an easy form process that gives the user some options or dropdowns to complete before submission – up to 3 would be sufficient.
o Require their name and contact details.

NOTE: Images to follow:

Target Market(s)

VENDRO's audience consists of businesses in mobile money, gaming, FMCG, beverage, and alcohol sectors, primarily Business Development Managers or Operations Managers who are seeking insight into their respective marketplaces.

Industry/Entity Type

VENDRO is a premier consulting firm that specialises in aiding global corporations and emerging businesses to enter and scale within Africa's dynamic markets

Coding

Coded - Design and coding required

Number of Pages Required

5+ page

Font styles to use
Sans Serif
Other font styles liked:
• Poppins Font Family

Colors

Designer to choose colors to be used in the design.

Requirements
Must have
• The primary goal is to present a clear and concise picture of our consulting firm, and it's specialisation in Africa - smooth and crisp UI with animations or transitions that imply we know our way around tecchnology is always helpful - but a Clean and responsive UI is most important.
Nice to have
• Reactive and animated transitions through sections or pages - not overdone - adds a professional feel to the site
Should not have
• We don't want too many colours, and we don't want it too dark - we want a monochrome theme, with accents of colour when relevant

```html
<!DOCTYPE html>
<html lang="en">
<head>
<meta charset="utf-8">
<title>Vendro Sahel – Home</title>
<link href="https://fonts.googleapis.com/css2?family=Poppins:wght@300;400;500;600;700;800&display=swap" rel="stylesheet">
<style>
:root{
  --ink:#000;
  --paper:#fff;
  --line:#333;
  --frame-grey:rgba(200,200,200,.6);
  --hero-a:#2b2e33;
  --hero-b:#3d3a38;
  --footer-faint:rgba(255,255,255,.12);
}
*{box-sizing:border-box;margin:0;padding:0}
html,body{width:1200px;height:3061px;overflow:hidden;background:var(--paper)}
body{font-family:'Poppins',sans-serif;color:var(--ink);position:relative}
.abs{position:absolute}

/* header */
.site-header{position:absolute;left:0;top:0;width:1200px;height:83px;background:var(--paper)}
.brand{position:absolute;left:112px;top:18px;display:flex;align-items:center;gap:10px}
.brand-mark{width:44px;height:44px;background:var(--ink)}
.brand-name{font-size:42px;font-weight:500;letter-spacing:1px;line-height:1}
.main-nav a{position:absolute;top:0;height:83px;line-height:83px;font-size:16px;color:var(--ink);text-decoration:none}
.main-nav a.active{background:var(--ink);color:var(--paper);width:72px;text-align:center;font-weight:500}
.header-icons svg{position:absolute}

/* hero */
.hero{position:absolute;left:0;top:83px;width:1200px;height:515px;background:linear-gradient(100deg,var(--hero-a),#4a4644 45%,#2f3a45 75%,var(--hero-b))}
.hero-frame{position:absolute;left:187px;top:75px;width:820px;height:365px;border:3px solid var(--frame-grey)}
.hero-title{position:absolute;left:0;width:1152px;top:96px;text-align:center;color:var(--paper);font-size:55px;font-weight:700;line-height:71px}
.hero-sub{position:absolute;left:0;width:1196px;top:240px;text-align:center;color:var(--paper);font-size:27px;font-weight:300;line-height:39px}
.hero svg{position:absolute}

/* about */
.about-frame{position:absolute;left:303px;top:684px;width:293px;height:300px;background:var(--ink)}
.about-frame::after{content:"";position:absolute;left:22px;top:24px;width:247px;height:250px;background:var(--paper)}
.about-photo{position:absolute;left:112px;top:719px;width:451px;height:443px;background:linear-gradient(160deg,#6f6e6a,#3f4650 55%,#5a6a7c)}
.section-title{font-weight:700;font-size:40px;line-height:1.1}
.body-copy{font-size:15.6px;line-height:25.7px;font-weight:400}
.btn{position:absolute;display:flex;align-items:center;justify-content:center;font-size:19px;font-weight:400}
.btn::before{content:"";position:absolute;inset:5px;border:2px solid currentColor}
.btn-dark{background:var(--ink);color:var(--paper)}
.btn-light{background:var(--paper);color:var(--ink)}

/* services */
.services-title{position:absolute;left:0;width:1200px;top:1243px;text-align:center;font-size:42px;font-weight:700}
.service-card{position:absolute;top:1351px;width:277px;height:281px}
.service-card .tl{position:absolute;left:0;top:0;width:263px;height:208px;border-left:14px solid var(--ink);border-top:14px solid var(--ink)}
.service-card .br{position:absolute;right:0;bottom:0;width:234px;height:267px;border-right:14px solid var(--ink);border-bottom:14px solid var(--ink)}
.service-card svg.icon{position:absolute;left:106px;top:42px}
.service-card h3{position:absolute;left:0;width:277px;top:122px;text-align:center;font-size:21px;font-weight:600;line-height:31px}
.service-card .go{position:absolute;left:124px;top:207px;width:29px;height:29px;background:var(--ink)}

/* process */
.process{position:absolute;left:0;top:1719px;width:1200px;height:479px;background:var(--ink)}
.process-photo{position:absolute;left:0;top:0;width:596px;height:479px;background:linear-gradient(200deg,#f3d9a4,#9aa7b8 35%,#4e5866 70%,#2c3440)}
.process .section-title{position:absolute;left:691px;top:47px;color:var(--paper);font-size:42px}
.process .body-copy{position:absolute;left:691px;width:410px;color:var(--paper);font-size:16px}

/* contact + footer */
.footer-band{position:absolute;left:0;top:2614px;width:1200px;height:447px;background:var(--ink)}
.contact-card{position:absolute;left:112px;top:2285px;width:974px;height:471px;background:var(--paper);box-shadow:0 0 14px rgba(0,0,0,.18)}
.contact-photo{position:absolute;left:50px;top:60px;width:300px;height:352px;background:linear-gradient(180deg,#2f5563,#7b8890 45%,#c8c8c4)}
.contact-card .section-title{position:absolute;left:404px;top:38px;font-size:42px}
.contact-card .body-copy{position:absolute;left:405px;top:94px;width:540px}
.field{position:absolute;border-bottom:1.5px solid var(--line);font-size:15.5px;height:34px}
.footer-col{position:absolute;top:2810px;color:var(--paper)}
.footer-col h4{font-size:21px;font-weight:600;margin-bottom:9px}
.footer-col p{font-size:14px;line-height:22.6px}
.footer-ghost{position:absolute;left:445px;top:2832px;font-size:84px;font-weight:600;color:var(--footer-faint);letter-spacing:4px}
.newsletter-line{position:absolute;left:850px;top:2880px;width:236px;border-bottom:1.5px solid var(--paper)}
.social{position:absolute;top:2908px;display:flex;align-items:center;gap:6px;color:var(--paper);font-size:13px}
.social i{display:block;width:18px;height:18px;border:2px solid var(--paper);border-radius:50%}
.footer-rule{position:absolute;left:0;top:3002px;width:1200px;border-top:1px solid #555}
.copyright{position:absolute;left:0;width:1200px;top:3022px;text-align:center;color:var(--paper);font-size:14px}
</style>
</head>
<body>

<header class="site-header">
  <div class="brand"><span class="brand-mark"></span><span class="brand-name">VENDRO</span></div>
  <nav class="main-nav">
    <a class="active" href="#" style="left:457px">Home</a>
    <a href="#" style="left:545px">About</a>
    <a href="#" style="left:620px">Services</a>
    <a href="#" style="left:713px">Team</a>
    <a href="#" style="left:786px">Contact</a>
  </nav>
  <div class="header-icons">
    <svg style="left:995px;top:24px" width="30" height="34" viewBox="0 0 30 34"><circle cx="15" cy="9" r="8" fill="#000"/><path d="M1 33c0-9 6-13 14-13s14 4 14 13z" fill="#000"/></svg>
    <svg style="left:1058px;top:27px" width="30" height="30" viewBox="0 0 30 30"><circle cx="11" cy="11" r="8.5" fill="none" stroke="#000" stroke-width="3"/><path d="M17 17l11 11" stroke="#000" stroke-width="4" stroke-linecap="round"/></svg>
  </div>
</header>

<section class="hero" role="img" aria-label="Team of five business professionals standing arms crossed before a wall of world clocks">
  <div class="hero-frame"></div>
  <h1 class="hero-title">Welcome to<br>Vendro</h1>
  <p class="hero-sub">Duis aute irure dolor in reprehenderit in voluptate<br>velit esse cillum dolore eu fugiat nulla pariatur.</p>
  <svg style="left:545px;top:345px" width="62" height="62" viewBox="0 0 62 62"><circle cx="31" cy="31" r="28" fill="none" stroke="#fff" stroke-width="4"/><path d="M25 19l17 12-17 12z" fill="#fff"/></svg>
  <svg style="left:88px;top:240px" width="24" height="38" viewBox="0 0 24 38"><path d="M20 3L5 19l15 16" fill="none" stroke="#fff" stroke-width="4"/></svg>
  <svg style="left:1088px;top:240px" width="24" height="38" viewBox="0 0 24 38"><path d="M4 3l15 16L4 35" fill="none" stroke="#fff" stroke-width="4"/></svg>
</section>

<section class="about">
  <div class="about-frame"></div>
  <div class="about-photo" role="img" aria-label="Smiling businesswoman with arms crossed in a modern office"></div>
  <h2 class="section-title abs" style="left:672px;top:708px">About Us</h2>
  <p class="body-copy abs" style="left:673px;top:779px;width:416px">Lorem ipsum dolor sit amet, consectetur adipiscing elit, sed do eiusmod tempor incididunt ut labore et dolore magna aliqua. Ut enim ad minim veniam, quis nostrud exercitation ullamco laboris nisi ut aliquip ex ea commodo consequat.</p>
  <p class="body-copy abs" style="left:673px;top:934px;width:416px">Duis aute irure dolor in reprehenderit in voluptate velit esse cillum dolore eu fugiat nulla pariatur. Excepteur sint occaecat cupidatat non proident, sunt in culpa qui officia deserunt mollit anim id est laborum.</p>
  <a class="btn btn-dark" style="left:672px;top:1091px;width:141px;height:42px">Read More</a>
</section>

<section class="services">
  <h2 class="services-title">Our Services</h2>
  <svg class="abs" style="left:62px;top:1480px" width="24" height="38" viewBox="0 0 24 38"><path d="M20 3L5 19l15 16" fill="none" stroke="#000" stroke-width="4"/></svg>
  <svg class="abs" style="left:1114px;top:1480px" width="24" height="38" viewBox="0 0 24 38"><path d="M4 3l15 16L4 35" fill="none" stroke="#000" stroke-width="4"/></svg>

  <article class="service-card" style="left:110px">
    <div class="tl"></div><div class="br"></div>
    <svg class="icon" width="64" height="64" viewBox="0 0 64 64" fill="none" stroke="#000" stroke-width="2"><circle cx="20" cy="24" r="14"/><circle cx="20" cy="24" r="6"/><rect x="40" y="8" width="18" height="8"/><rect x="40" y="22" width="18" height="8"/><rect x="40" y="36" width="18" height="8"/><rect x="40" y="50" width="18" height="8"/><path d="M34 24h6M20 38v16h20M30 40h10"/></svg>
    <h3>Identify Growth<br>Pathways</h3>
    <span class="go"></span>
  </article>

  <article class="service-card" style="left:460px">
    <div class="tl"></div><div class="br"></div>
    <svg class="icon" width="64" height="64" viewBox="0 0 64 64" fill="none" stroke="#000" stroke-width="2"><path d="M32 2l11 6v12l-11 6-11-6V8z"/><path d="M21 8l11 6 11-6M32 14v12M32 26v10M14 40l18-4 18 4"/><circle cx="12" cy="46" r="4"/><circle cx="32" cy="46" r="4"/><circle cx="52" cy="46" r="4"/><path d="M5 62v-6a7 7 0 0114 0v6M25 62v-6a7 7 0 0114 0v6M45 62v-6a7 7 0 0114 0v6"/></svg>
    <h3>Drive Customer<br>Demand</h3>
    <span class="go"></span>
  </article>

  <article class="service-card" style="left:810px">
    <div class="tl"></div><div class="br"></div>
    <svg class="icon" width="64" height="70" viewBox="0 0 64 70" fill="none" stroke="#000" stroke-width="2"><path d="M32 6a20 20 0 00-12 36v8h24v-8A20 20 0 0032 6z"/><path d="M22 54h20M24 59h16M27 64h10M32 12v30M24 20c-4 4-2 10 2 12M40 20c4 4 2 10-2 12M2 26h6M56 26h6M8 8l5 5M56 8l-5 5"/></svg>
    <h3>Reimagine<br>Brands</h3>
    <span class="go"></span>
  </article>
</section>

<section class="process">
  <div class="process-photo" role="img" aria-label="Glass office towers seen from below in warm sunlight"></div>
  <h2 class="section-title">Our Process</h2>
  <p class="body-copy" style="top:126px">Lorem ipsum dolor sit amet, consectetur adipiscing elit, sed do eiusmod tempor incididunt ut labore et dolore magna aliqua. Ut enim ad minim veniam, quis nostrud exercitation ullamco laboris nisi ut aliquip ex ea commodo consequat.</p>
  <p class="body-copy" style="top:282px">Duis aute irure dolor in reprehenderit in voluptate velit esse cillum dolore eu fugiat nulla pariatur.</p>
  <a class="btn btn-light" style="left:690px;top:384px;width:141px;height:42px">Read More</a>
</section>

<div class="footer-band"></div>

<section class="contact-card">
  <div class="contact-photo" role="img" aria-label="Businesswoman checking her phone outside an office building"></div>
  <h2 class="section-title">Contact Us</h2>
  <p class="body-copy">Excepteur sint occaecat cupidatat non proident, sunt in culpa qui officia deserunt mollit anim id est laborum.</p>
  <div class="field" style="left:401px;top:171px;width:221px">First Name</div>
  <div class="field" style="left:697px;top:171px;width:220px">Last Name</div>
  <div class="field" style="left:401px;top:241px;width:221px">E-Mail</div>
  <div class="field" style="left:697px;top:241px;width:220px">Phone</div>
  <div class="field" style="left:401px;top:310px;width:516px">Message</div>
  <a class="btn btn-dark" style="left:402px;top:385px;width:103px;height:42px">Submit</a>
</section>

<footer>
  <div class="footer-ghost">VENDRO</div>
  <div class="footer-col" style="left:112px"><h4>Company</h4><p>Lorem ipsum dolor sit<br>amet, consectetur<br>adipiscing&nbsp; tempor</p></div>
  <div class="footer-col" style="left:377px"><h4>Address</h4><p>&nbsp;no,742 Vendro,Lorem<br>ipsum dolor sit amet<br>na,418273.<br>+1 555-014-2290</p></div>
  <div class="footer-col" style="left:668px"><h4>Links</h4><p>Home<br>About<br>Services<br>Team<br>Contact</p></div>
  <div class="footer-col" style="left:850px"><h4>Newsletter</h4>
    <p style="font-size:9px;display:flex;align-items:center;gap:6px;width:236px"><svg width="14" height="10" viewBox="0 0 14 10"><rect x=".5" y=".5" width="13" height="9" fill="none" stroke="#fff"/><path d="M1 1l6 5 6-5" fill="none" stroke="#fff"/></svg>Enter Your Email Id<svg style="margin-left:auto" width="22" height="10" viewBox="0 0 22 10"><path d="M0 5h20M16 1l4 4-4 4" fill="none" stroke="#fff" stroke-width="1.5"/></svg></p>
  </div>
  <div class="newsletter-line"></div>
  <a class="social" style="left:853px"><i></i>Picsnap</a>
  <a class="social" style="left:940px"><i></i>Workhive</a>
  <div class="footer-rule"></div>
  <p class="copyright">Copyright © 2023&nbsp; Vendro.All rights reserved.Privacy Policy</p>
</footer>

</body>
</html>
```